Real Estate Renovation and Rental:Business Card/Logo Design Project

Corliss Grove LLC is a small partnership that buys homes to renovate, then provide as rentals to people who may not currently be able to purchase a home - but we also coach them on how to improve their credit so that, in 2-5 years, they may be able to buy a home. Maybe even the one they're living in.

We are based in Sonoma County of Northern California, operating in communities including Healdsburg, Windsor, Santa Rosa, and Cloverdale.

Please design a business card, but the same logo should work for signs that we will post on the homes as they are being renovated.

The design should be clean, contemporary, professional but warm. I'd love to see a rooftop feature, or some other element of a house. Again, not too much detail, clean and welcoming. The design must include "Corliss Grove LLC" - but "CGLLC" could also be used as a primary name, with "Corliss Grove LLC" in smaller print somewhere. If using "CGLLC", the CG could be visually distinct (larger, different color, font) than the LLC part of the name but they must be together.
Updates

just conferring with partner to choose a final design ... should be ready to choose soon and will post

Industry/Entity Type

Business

Requirements
Must have
• the name "Corliss Grove LLC"
for business card design, and leave room for us to customize with partner names, address, telephone numbers, email addresses
Nice to have
• some element of a house included

```html
<!DOCTYPE html>
<html lang="en">
<head>
<meta charset="utf-8">
<title>Corliss Grove LLC — Business Card</title>
<link href="https://fonts.googleapis.com/css2?family=Arimo:wght@400;700&display=swap" rel="stylesheet">
<style>
  :root {
    --stage-light: #f7f7f7;
    --stage-dark: #cfcfcf;
    --card-white: #ffffff;
    --brand-blue: #1b4f9e;
    --brand-green: #008a2e;
    --accent-green-light: #5cb531;
    --back-top: #0a84da;
    --back-mid: #033d8a;
    --back-bottom: #1f1562;
    --url-blue: #1d4f9a;
  }
  * { margin: 0; padding: 0; box-sizing: border-box; }
  html, body { width: 1200px; height: 900px; overflow: hidden; }
  body {
    font-family: "Arimo", Arial, sans-serif;
    background: radial-gradient(ellipse at center, var(--stage-light) 0%, var(--stage-light) 35%, var(--stage-dark) 100%);
    position: relative;
  }
  .card {
    position: absolute;
    left: 274px;
    width: 652px;
    height: 331px;
    border-radius: 22px;
    overflow: hidden;
  }
  .card-front { top: 101px; background: var(--card-white); }
  .card-back {
    top: 468px;
    background: linear-gradient(180deg, var(--back-top) 0%, var(--back-mid) 62%, var(--back-bottom) 100%);
  }
  .front-band {
    position: absolute;
    left: 0; top: 267px;
    width: 563px; height: 64px;
    background: var(--brand-green);
  }
  .front-rule {
    position: absolute;
    left: 553px; top: 0;
    width: 10px; height: 331px;
    background: linear-gradient(180deg, var(--accent-green-light) 0%, var(--brand-green) 100%);
  }
  .front-url {
    position: absolute;
    left: 606px; top: 170px;
    transform: translate(-50%, -50%) rotate(-90deg);
    font-size: 13px;
    letter-spacing: 1.6px;
    color: var(--url-blue);
    white-space: nowrap;
  }
  .brand {
    position: absolute;
    display: flex;
    align-items: flex-start;
    gap: 8px;
  }
  .brand-square { width: 66px; height: 66px; flex: none; }
  .brand-name { display: flex; flex-direction: column; font-weight: 700; }
  .brand-short { font-size: 68px; line-height: 52px; letter-spacing: -1px; }
  .brand-full { font-size: 17px; line-height: 17px; margin-top: 2px; padding-left: 2px; }
  .card-front .brand { left: 30px; top: 29px; color: var(--brand-blue); }
  .card-front .brand-square { background: var(--brand-blue); }
  .card-back .brand { left: 171px; top: 133px; color: var(--card-white); }
  .card-back .brand-square { background: var(--card-white); }
</style>
</head>
<body>
  <section class="card card-front" aria-label="Business card front">
    <div class="brand">
      <div class="brand-square"></div>
      <div class="brand-name">
        <span class="brand-short">CGLLC</span>
        <span class="brand-full">Corliss Grove LLC</span>
      </div>
    </div>
    <div class="front-band"></div>
    <div class="front-rule"></div>
    <div class="front-url">WWW.WEBSITE.COM</div>
  </section>

  <section class="card card-back" aria-label="Business card back">
    <div class="brand">
      <div class="brand-square"></div>
      <div class="brand-name">
        <span class="brand-short">CGLLC</span>
        <span class="brand-full">Corliss Grove LLC</span>
      </div>
    </div>
  </section>
</body>
</html>
```